Marlowe Holdings LLC - Business Cards

Need the following information on the cards:

Name: Dean R Vossler
Title: Chief Executive Manager

Business address:
412 N Ridgeview Lane #118
Linden Falls, Mn 60412

Phone: (507) 555-0148 - Business
KPV FFL license number: 5-21-xxx-xx-xx-04519
Email: dean.vossler@marloweholdingsffl.com

Target Market(s)

Firearm owners

Industry/Entity Type

Firearms industry,

Contact Information for Business Card

Contact number, name and title, web page address, email, business address and kpv license number,

Requirements
Must have
• Name, title, business address, phone numbers, KPV license numbers, web page address and email address.
Nice to have
• Cellphone number,

```html
<!DOCTYPE html>
<html lang="en">
<head>
<meta charset="utf-8">
<title>Marlowe Holdings LLC – Business Cards</title>
<link rel="stylesheet" href="https://fonts.googleapis.com/css2?family=Tinos:wght@400;700&display=swap">
<style>
  :root {
    --stage: #3a3a3c;
    --card: #1f1d1e;
    --red: #c8171e;
    --white: #f2f0ee;
    --rule: #b0141a;
  }
  * { margin: 0; padding: 0; box-sizing: border-box; }
  html, body { width: 1200px; height: 900px; overflow: hidden; }
  body {
    background: var(--stage);
    font-family: "Tinos", "Times New Roman", serif;
    position: relative;
  }
  .card {
    position: absolute;
    width: 640px;
    height: 366px;
    background: var(--card);
    overflow: hidden;
    box-shadow: 0 14px 30px rgba(0,0,0,.45);
  }
  .card--front { left: 170px; top: 50px; }
  .card--back  { left: 390px; top: 484px; }
  .band { position: absolute; left: 0; top: 0; width: 640px; height: 366px; }

  .brand-mark {
    position: absolute;
    display: flex;
    align-items: center;
    gap: 10px;
    color: var(--red);
    font-weight: 700;
    font-size: 22px;
    letter-spacing: .5px;
    white-space: nowrap;
  }
  .brand-mark__dot {
    width: 16px; height: 16px; border-radius: 50%;
    background: var(--red);
    flex: none;
  }
  .card--front .brand-mark { right: 34px; top: 92px; }
  .card--back .brand-mark { right: 28px; top: 58px; font-size: 18px; }

  .web-address {
    position: absolute; left: 34px; top: 36px;
    color: var(--white); font-size: 17px; letter-spacing: .3px;
  }
  .web-address span { color: var(--red); }

  .dog-art {
    position: absolute;
    background: linear-gradient(160deg, rgba(200,23,30,.55), rgba(200,23,30,.15));
    border-radius: 6px;
  }
  .card--front .dog-art { left: 50px; top: 160px; width: 120px; height: 150px; }
  .card--back .dog-art { left: 430px; top: 150px; width: 190px; height: 100px; }

  .person { position: absolute; left: 40px; top: 40px; }
  .person__name { color: var(--red); font-weight: 700; font-size: 24px; }
  .person__title { color: var(--white); font-size: 17px; margin-top: 2px; }

  .contact-list {
    position: absolute; left: 40px; top: 152px;
    list-style: none; color: var(--white); font-size: 15px;
  }
  .contact-list li { display: flex; align-items: center; gap: 10px; height: 25px; white-space: nowrap; }
  .contact-list svg { width: 14px; height: 14px; fill: var(--red); flex: none; }
  .contact-rule {
    position: absolute; left: 40px; top: 255px; width: 380px; height: 1px;
    background: var(--rule);
  }
  .contact-address { position: absolute; left: 40px; top: 268px; }
  .license {
    position: absolute; left: 40px; bottom: 13px;
    color: var(--white); font-size: 17px; letter-spacing: .3px;
  }
</style>
</head>
<body>

  <section class="card card--front" aria-label="Card front">
    <svg class="band" viewBox="0 0 640 366" aria-hidden="true">
      <path d="M0 316 C220 316 330 250 640 196 L640 366 L0 366 Z" fill="var(--red)"/>
    </svg>
    <p class="web-address">www.<span>marloweholdingsffl</span>.com</p>
    <div class="brand-mark"><span class="brand-mark__dot"></span>Marlowe Holdings LLC</div>
    <div class="dog-art" role="img" aria-label="Red line illustration of a shepherd dog sitting and looking up"></div>
  </section>

  <section class="card card--back" aria-label="Card back">
    <svg class="band" viewBox="0 0 640 366" aria-hidden="true">
      <path d="M0 322 L340 322 C440 322 500 262 640 246 L640 366 L0 366 Z" fill="var(--red)"/>
    </svg>
    <div class="brand-mark"><span class="brand-mark__dot"></span>Marlowe Holdings LLC</div>
    <div class="dog-art" role="img" aria-label="Red line illustration of a standing shepherd dog"></div>

    <div class="person">
      <p class="person__name">Dean R Vossler</p>
      <p class="person__title">Chief Executive Manager</p>
    </div>

    <ul class="contact-list">
      <li>
        <svg viewBox="0 0 14 14"><path d="M3 0h8v14H3z M4.5 1.5v10h5v-10z" fill-rule="evenodd"/></svg>
        (507) 555-0148
      </li>
      <li>
        <svg viewBox="0 0 14 14"><circle cx="7" cy="7" r="6.5"/></svg>
        www.marloweholdingsffl.com
      </li>
      <li>
        <svg viewBox="0 0 14 14"><path d="M0 3h14v9H0z M1 4l6 4 6-4v-.2H1z" fill-rule="evenodd"/></svg>
        dean.vossler@marloweholdingsffl.com
      </li>
    </ul>
    <div class="contact-rule"></div>
    <ul class="contact-list contact-address">
      <li>
        <svg viewBox="0 0 14 14"><path d="M7 0a5 5 0 0 1 5 5c0 3.5-5 9-5 9S2 8.5 2 5a5 5 0 0 1 5-5z M7 3a2 2 0 1 0 0 4a2 2 0 1 0 0-4z" fill-rule="evenodd"/></svg>
        412 N Ridgeview Lane #118, Linden Falls, Mn 60412
      </li>
    </ul>

    <p class="license">KPV FFL License Number: 5-21-xxx-xx-xx-04519</p>
  </section>

</body>
</html>
```